Watch brand needs new business cards

Kestrel Timepiece Company are looking for a new business card design incorporating our logo and brand colours as per our website.

Design should be 90x55mm with 3mm print margin from edges and 3mm external bleed.

Card should be double sided, e.g. logo one side, personal details on the other.

Logo will be provided as a vector.

The card must be able to show:
- Staff name
- Position
- Office Address
- Email
- Telephone number
- Website address

Final work must be provided in an editable format to allow us to add staff details (e.g. an AI or PSD file).

```html
<!DOCTYPE html>
<html lang="en">
<head>
<meta charset="utf-8">
<title>Kestrel Timepiece Company – Business Cards</title>
<link rel="stylesheet" href="https://fonts.googleapis.com/css2?family=Quicksand:wght@400;500;700&display=swap">
<style>
  :root {
    --bg: #ece9e4;
    --kraft: #c9a274;
    --card-white: #f4f4f5;
    --ink: #1d1d1f;
    --ink-soft: #3a3a3c;
    --shadow: rgba(60, 45, 30, 0.18);
  }
  * { box-sizing: border-box; margin: 0; padding: 0; }
  html, body {
    width: 1200px; height: 801px; overflow: hidden;
    background: var(--bg);
    font-family: "Quicksand", sans-serif;
    color: var(--ink);
  }
  .canvas {
    position: relative; width: 1200px; height: 801px;
    display: flex; align-items: center; justify-content: center; gap: 56px;
  }
  .card {
    width: 520px; height: 318px;
    border-radius: 4px;
    box-shadow: 0 10px 28px var(--shadow);
    position: relative;
  }
  .card--front {
    background: var(--kraft);
    display: flex; align-items: center; justify-content: center;
  }
  .card--back {
    background: var(--card-white);
    display: flex; align-items: center;
    padding: 0 34px 0 36px;
  }
  .brand {
    display: flex; flex-direction: column; align-items: center; gap: 14px;
    font-weight: 700; color: var(--ink);
  }
  .brand__circle {
    width: 64px; height: 64px; border-radius: 50%;
    border: 4px solid var(--ink);
  }
  .brand__name {
    font-size: 26px; letter-spacing: 0.04em; text-align: center; line-height: 1.15;
  }
  .card--front .brand__circle { width: 80px; height: 80px; border-width: 5px; }
  .card--front .brand__name { font-size: 32px; }
  .card__brand-side { width: 240px; display: flex; justify-content: center; }
  .card--back .brand__name { font-size: 21px; }
  .divider {
    width: 3px; height: 190px; background: var(--ink); margin: 0 22px 0 16px;
  }
  .details { flex: 1; }
  .staff-name { font-size: 28px; font-weight: 400; line-height: 1; }
  .staff-name strong { font-weight: 700; }
  .job-title { font-size: 16px; color: var(--ink-soft); margin: 4px 0 22px; }
  .contact-list { list-style: none; display: flex; flex-direction: column; gap: 8px; }
  .contact-list li {
    display: flex; align-items: center; gap: 12px; font-size: 16px; font-weight: 500;
  }
  .contact-list svg { width: 16px; height: 16px; flex: none; fill: var(--ink); }
</style>
</head>
<body>
<main class="canvas">
  <section class="card card--front" aria-label="Card front">
    <div class="brand">
      <span class="brand__circle"></span>
      <span class="brand__name">KESTREL<br>TIMEPIECE COMPANY</span>
    </div>
  </section>

  <section class="card card--back" aria-label="Card back">
    <div class="card__brand-side">
      <div class="brand">
        <span class="brand__circle"></span>
        <span class="brand__name">KESTREL<br>TIMEPIECE COMPANY</span>
      </div>
    </div>
    <div class="divider"></div>
    <div class="details">
      <p class="staff-name">Staff <strong>Name</strong></p>
      <p class="job-title">Job Title</p>
      <ul class="contact-list">
        <li>
          <svg viewBox="0 0 16 16" aria-hidden="true"><path d="M8 1a5 5 0 0 0-5 5c0 3.6 5 9 5 9s5-5.4 5-9a5 5 0 0 0-5-5zm0 7a2 2 0 1 1 0-4 2 2 0 0 1 0 4z"/></svg>
          Office Address
        </li>
        <li>
          <svg viewBox="0 0 16 16" aria-hidden="true"><path d="M1 3h14v1.2L8 9 1 4.2z"/><path d="M1 5.6 8 10.4l7-4.8V13H1z"/></svg>
          Email
        </li>
        <li>
          <svg viewBox="0 0 16 16" aria-hidden="true"><path d="M1 6c0-2 3-3.5 7-3.5S15 4 15 6v1.5h-3.5V6h-7v1.5H1z"/><path d="M3 9h10l1 5H2z"/></svg>
          Telephone number
        </li>
        <li>
          <svg viewBox="0 0 16 16" aria-hidden="true" style="fill:none;stroke:var(--ink);stroke-width:1.2"><circle cx="8" cy="8" r="6.5"/><ellipse cx="8" cy="8" rx="2.8" ry="6.5"/><path d="M1.5 8h13M2.5 4.8h11M2.5 11.2h11"/></svg>
          Website address
        </li>
      </ul>
    </div>
  </section>
</main>
</body>
</html>
```